Design for schnapps bottle label "El Sendero"

Hi! On a small land lot we are producing our own Italian schnapps "Grappa". For the bottles we would like to modernize our current labes that you find below. The two cats looking at each other should remain, but updated and more modern. I am very much looking forward to your suggestions. Best, Tobias

Target Market(s)

Schnapps bottle label

Requirements
Must have
• Cats should resemble the cats that are decorating the house entry (see attached), however, should have a more modern appearance.

Text elements should remain: "Grappa", "El Sendero", "Legnoso", "[Vintage Year], "Raccolta No", "Vol %"
Should not have
• Current ornament can be used, replaced or deleted (whatever looks best)

```html
<!DOCTYPE html>
<html lang="it">
<head>
<meta charset="utf-8">
<title>Grappa Legnoso 2015 – El Sendero</title>
<link rel="stylesheet" href="https://fonts.googleapis.com/css2?family=Fredoka:wght@600&family=Bebas+Neue&family=Roboto:wght@400&family=Roboto+Condensed:wght@500&display=swap">
<style>
  :root {
    --orange: #f58f22;
    --orange-deep: #f07c0f;
    --ink: #3a3838;
  }
  html, body {
    margin: 0;
    padding: 0;
    overflow: hidden;
    background: var(--orange);
  }
  .label {
    position: relative;
    width: 851px;
    height: 1200px;
    background: var(--orange);
    overflow: hidden;
    color: var(--ink);
  }
  .label__swoosh {
    position: absolute;
    inset: 0;
  }
  .label__title {
    position: absolute;
    left: 0;
    top: 0;
  }
  .title-grappa {
    font-family: "Fredoka", sans-serif;
    font-weight: 600;
    font-size: 250px;
  }
  .title-variety {
    font-family: "Bebas Neue", sans-serif;
    font-size: 96px;
  }
  .label__cats {
    position: absolute;
    left: 58px;
    top: 436px;
    width: 735px;
    height: 362px;
    background: var(--ink);
    border-radius: 160px 160px 24px 24px;
    opacity: 0.9;
  }
  .label__by {
    position: absolute;
    left: 0;
    right: 0;
    top: 810px;
    text-align: center;
    font-family: "Roboto Condensed", sans-serif;
    font-weight: 500;
    font-size: 15px;
    letter-spacing: 0.5px;
    line-height: 1;
  }
  .label__producer {
    position: absolute;
    left: 0;
    right: 0;
    top: 850px;
    text-align: center;
    font-family: "Roboto Condensed", sans-serif;
    font-weight: 500;
    font-size: 56px;
    letter-spacing: 1px;
    text-transform: uppercase;
    line-height: 1;
  }
  .label__meta {
    position: absolute;
    bottom: 40px;
    font-family: "Roboto", sans-serif;
    font-weight: 400;
    font-size: 40px;
    line-height: 1;
  }
  .label__batch { left: 34px; }
  .label__abv { right: 38px; }
</style>
</head>
<body>
<main class="label">
  <svg class="label__swoosh" width="851" height="1200" viewBox="0 0 851 1200" aria-hidden="true">
    <path fill="var(--orange-deep)" d="M0 285 C330 230 610 430 612 760 C614 960 470 1120 275 1190 C400 1050 440 900 436 760 C430 540 230 375 0 367 Z"/>
  </svg>

  <svg class="label__title" width="851" height="400" viewBox="0 0 851 400">
    <defs>
      <pattern id="hatch" width="4" height="4" patternUnits="userSpaceOnUse" patternTransform="rotate(-45)">
        <rect width="4" height="4" fill="var(--orange)"/>
        <rect width="4" height="1.6" fill="var(--ink)"/>
      </pattern>
    </defs>
    <g class="title-grappa">
      <text x="112" y="287" textLength="614" lengthAdjust="spacingAndGlyphs" fill="url(#hatch)">GRAPPA</text>
      <text x="126" y="272" textLength="614" lengthAdjust="spacingAndGlyphs" fill="var(--orange)" stroke="var(--ink)" stroke-width="10" stroke-linejoin="round" paint-order="stroke">GRAPPA</text>
    </g>
    <g class="title-variety">
      <text x="218" y="380" textLength="403" lengthAdjust="spacingAndGlyphs" fill="url(#hatch)">LEGNOSO 2015</text>
      <text x="224" y="373" textLength="403" lengthAdjust="spacingAndGlyphs" fill="var(--orange)" stroke="var(--ink)" stroke-width="5" stroke-linejoin="round" paint-order="stroke">LEGNOSO 2015</text>
    </g>
  </svg>

  <div class="label__cats" role="img" aria-label="Illustration of two dark silhouetted cats with arched backs and raised tails, facing each other"></div>

  <div class="label__by">DI</div>
  <div class="label__producer">El Sendero</div>

  <div class="label__meta label__batch">Raccolta No.1</div>
  <div class="label__meta label__abv">41.0% Vol.</div>
</main>
</body>
</html>
```